Carton Box Packaging For Motorcycle Electric Regulator - Brevora Brand

Packaging Dimensions: 7cm (H) x 6cm (W) x 2.5cm (D)
We would like to design a genuine Carton box Packaging for motorcycle electric regulator.
This is a sensitive part of the motorcycle, so we need the packaging to reflect elegant impression.
Brevora, is one of the leading companies for manufacturing Motorcycles, located in Egypt. Our company is offering high-quality products, the best in the local market, with very competitive prices.
We have a limited time to get this project done, So we Highly appreciate receiving your designs ASAP.
Target Market(s)
Motorcycle Parts Buyers
Font styles to use
Colors
Designer to choose colors to be used in the design.
Look and feel
Each slider illustrates characteristics of the customer's brand and the style your logo design should communicate.

```html
<!DOCTYPE html>
<html lang="en">
<head>
<meta charset="utf-8">
<title>Brevora Motorcycle Regulator – Box Dieline</title>
<link rel="stylesheet" href="https://fonts.googleapis.com/css2?family=Exo+2:ital,wght@0,800;1,800;1,900&family=Open+Sans:wght@400&display=swap">
<style>
  :root {
    --paper: #ffffff;
    --ink: #1a1a1a;
    --black: #050505;
    --red: #d3202b;
    --red-dark: #a5141d;
    --silver-light: #f4f4f4;
    --silver-mid: #b9b9b9;
    --silver-dark: #6d6d6d;
    --white: #ffffff;
  }
  * { margin: 0; padding: 0; box-sizing: border-box; }
  html, body { width: 1200px; height: 1000px; overflow: hidden; background: var(--paper); }
  .canvas { position: relative; width: 1200px; height: 1000px; }

  .dimensions {
    position: absolute; left: 0; width: 1200px; top: 164px;
    text-align: center;
    font-family: "Open Sans", sans-serif; font-size: 20px; color: var(--ink);
  }

  .panel { position: absolute; overflow: hidden; }
  .panel > svg.panel-art { position: absolute; inset: 0; width: 100%; height: 100%; }

  .flap-top    { left: 450px; top: 205px; width: 300px; height: 123px; background: var(--black); }
  .flap-bottom { left: 450px; top: 700px; width: 300px; height: 125px; background: var(--black); }
  .face-front  { left: 450px; top: 340px; width: 300px; height: 350px; background: var(--black); }
  .side-left   { left: 314px; top: 340px; width: 122px; height: 350px; background: var(--red); }
  .side-right  { left: 763px; top: 340px; width: 123px; height: 350px; background: var(--red); }

  .brand-name {
    font-family: "Exo 2", sans-serif; font-weight: 800; font-style: normal;
    color: var(--silver-light); letter-spacing: 2px; text-transform: uppercase;
    white-space: nowrap;
  }
  .flap-top .brand-name, .flap-bottom .brand-name {
    position: absolute; left: 0; right: 0; top: 50%;
    text-align: center; font-size: 26px; line-height: 1;
  }
  .flap-bottom .brand-name { transform: translateY(-50%); }
  .flap-top .brand-name { transform: translateY(-50%) rotate(180deg); }

  .face-front .brand-lockup {
    position: absolute; left: 0; right: 0; top: 20px;
    display: flex; flex-direction: column; align-items: center; gap: 8px;
  }
  .brand-dot { width: 60px; height: 60px; border-radius: 50%; background: var(--silver-mid); }
  .face-front .brand-name { font-size: 20px; line-height: 1; }

  .product-title {
    font-family: "Exo 2", sans-serif; font-weight: 900; font-style: italic;
    color: var(--white); text-transform: uppercase; line-height: 0.95;
    text-shadow: 0 0 2px var(--black), 1px 1px 0 var(--black), -1px -1px 0 var(--black);
    white-space: nowrap;
  }
  .face-front .product-title {
    position: absolute; left: 0; right: 0; top: 150px;
    text-align: center; font-size: 22px; letter-spacing: 0.5px;
  }
  .product-photo { position: absolute; }
  .face-front .product-photo { left: 92px; top: 212px; width: 208px; height: 138px; }
  .quality-tag {
    position: absolute; left: 16px; top: 296px;
    font-family: "Exo 2", sans-serif; font-weight: 800;
    color: var(--white); font-size: 14px; line-height: 1.15; text-transform: uppercase;
  }

  .side-left .product-title, .side-right .product-title {
    position: absolute; top: 50%; left: 50%;
    width: 200px; text-align: center; font-size: 19px;
  }
  .side-left .product-title  { transform: translate(-50%, -50%) rotate(90deg); }
  .side-right .product-title { transform: translate(-50%, -50%) rotate(-90deg); }

  .side-brand {
    position: absolute; left: 0; right: 0;
    display: flex; align-items: center; justify-content: center;
  }
  .side-brand .brand-name { font-size: 13px; letter-spacing: 1px; }
  .side-left .side-brand { top: 50px; transform: rotate(90deg); }
  .side-right .side-brand { bottom: 50px; transform: rotate(-90deg); }

  .side-left .product-photo  { left: 14px; top: 270px; width: 64px; height: 64px; }
  .side-right .product-photo { left: 30px; top: 6px; width: 86px; height: 70px; }
</style>
</head>
<body>
<main class="canvas">
  <p class="dimensions">7cm (H) x 6cm (W) x 2.5cm (D)</p>

  <section class="panel flap-top">
    <span class="brand-name">Brevora</span>
  </section>

  <section class="panel side-left">
    <svg class="panel-art" viewBox="0 0 122 350" preserveAspectRatio="none" aria-hidden="true">
      <defs>
        <linearGradient id="sideShadeL" x1="0" y1="0" x2="1" y2="1">
          <stop offset="0" stop-color="#e02a33"/><stop offset="1" stop-color="#b2161f"/>
        </linearGradient>
      </defs>
      <rect width="122" height="350" fill="url(#sideShadeL)"/>
      <path d="M0,0 L122,0 L122,40 C80,30 40,20 0,28 Z" fill="#ffffff" opacity="0.18"/>
      <path d="M0,220 C40,250 80,270 122,275 L122,350 L0,350 Z" fill="#9c121a" opacity="0.5"/>
    </svg>
    <div class="side-brand"><span class="brand-name">Brevora</span></div>
    <h2 class="product-title">Motorcycle<br>Regulator</h2>
    <svg class="product-photo" viewBox="0 0 64 64" role="img" aria-label="Photo of the motorcycle voltage regulator with wires">
      <defs>
        <linearGradient id="partL" x1="0" y1="0" x2="1" y2="1">
          <stop offset="0" stop-color="#4a4a4a"/><stop offset="1" stop-color="#1c1c1c"/>
        </linearGradient>
      </defs>
      <rect x="4" y="6" width="56" height="52" rx="4" fill="url(#partL)"/>
    </svg>
  </section>

  <section class="panel face-front">
    <svg class="panel-art" viewBox="0 0 300 350" preserveAspectRatio="none" aria-hidden="true">
      <defs>
        <linearGradient id="silverBand" x1="0" y1="0" x2="1" y2="0">
          <stop offset="0" stop-color="#ffffff"/>
          <stop offset="0.45" stop-color="#d9d9d9"/>
          <stop offset="1" stop-color="#5e5e5e"/>
        </linearGradient>
        <linearGradient id="redFace" x1="0" y1="0" x2="1" y2="1">
          <stop offset="0" stop-color="#e0252f"/><stop offset="1" stop-color="#b0151e"/>
        </linearGradient>
      </defs>
      <path d="M0,215 C90,175 190,135 300,95 L300,138 C200,172 100,220 0,285 Z" fill="url(#silverBand)"/>
      <path d="M0,285 C100,220 200,172 300,138 L300,350 L0,350 Z" fill="url(#redFace)"/>
    </svg>
    <div class="brand-lockup">
      <span class="brand-dot"></span>
      <span class="brand-name">Brevora</span>
    </div>
    <h1 class="product-title">Motorcycle<br>Regulator</h1>
    <svg class="product-photo" viewBox="0 0 208 138" role="img" aria-label="Photo of the black finned motorcycle voltage regulator with coloured wires">
      <defs>
        <linearGradient id="partF" x1="0" y1="0" x2="1" y2="1">
          <stop offset="0" stop-color="#4a4a4a"/><stop offset="1" stop-color="#1a1a1a"/>
        </linearGradient>
      </defs>
      <rect x="0" y="0" width="172" height="138" rx="6" fill="url(#partF)"/>
    </svg>
    <p class="quality-tag">High<br>Quality</p>
  </section>

  <section class="panel side-right">
    <svg class="panel-art" viewBox="0 0 123 350" preserveAspectRatio="none" aria-hidden="true">
      <defs>
        <linearGradient id="sideShadeR" x1="1" y1="0" x2="0" y2="1">
          <stop offset="0" stop-color="#e02a33"/><stop offset="1" stop-color="#b2161f"/>
        </linearGradient>
      </defs>
      <rect width="123" height="350" fill="url(#sideShadeR)"/>
      <path d="M0,230 C40,250 80,262 123,262 L123,350 L0,350 Z" fill="#9c121a" opacity="0.5"/>
    </svg>
    <svg class="product-photo" viewBox="0 0 86 70" role="img" aria-label="Photo of the motorcycle voltage regulator with wires">
      <defs>
        <linearGradient id="partR" x1="0" y1="0" x2="1" y2="1">
          <stop offset="0" stop-color="#4a4a4a"/><stop offset="1" stop-color="#1c1c1c"/>
        </linearGradient>
      </defs>
      <rect x="0" y="2" width="70" height="66" rx="4" fill="url(#partR)"/>
    </svg>
    <h2 class="product-title">Motorcycle<br>Regulator</h2>
    <div class="side-brand"><span class="brand-name">Brevora</span></div>
  </section>

  <section class="panel flap-bottom">
    <span class="brand-name">Brevora</span>
  </section>
</main>
</body>
</html>
```